Independent IT Consulting Professional. Looking for a clean crisp, somewhat traditional design. I have also attached the initial off-the-shelf design from PrintNook. My company has grown quickly, and I would like to take the card to the next level. Should be sharp, mature, classy well laid-out and convey confidence. I don't think the off-the-shelf design does this. I like the logo I have for the time being, but if someone has something better in mind, I would be happy to consider an alternative. I would also like to see the color Cyan used in a small way, either with the logo or some other color treatment, as I feel like this is a modern color that I always liked, but never was able to make anything work with it.
Industry/Entity Type
It Company
Contact Information for Business Card
Garrett L. Ostrander
Owner
TechHollow Solutions
2817 Marwood Lane
Brevard, NY 13592
(917) 555-0147
gostrander@techhollowsolutions.example
www.techhollowsolutions.example
Tagline: Business Technology Services and Consulting

```html
<!DOCTYPE html>
<html lang="en">
<head>
<meta charset="utf-8">
<title>TechHollow Solutions – Business Card</title>
<link rel="stylesheet" href="https://fonts.googleapis.com/css2?family=Carlito:wght@400;700&display=swap">
<style>
  :root {
    --brand-blue: #2262ab;
    --ink: #1a1a1a;
    --muted: #6b6b6b;
    --paper: #ffffff;
    --backdrop: #d9d9d9;
    --accent-black: #000000;
  }
  * { margin: 0; padding: 0; box-sizing: border-box; }
  html, body { width: 1200px; height: 900px; overflow: hidden; }
  body {
    position: relative;
    background: var(--backdrop);
    font-family: "Carlito", "Calibri", sans-serif;
  }
  .card { position: absolute; width: 649px; height: 379px; overflow: hidden; }

  /* Front */
  .card-front { left: 112px; top: 38px; background: var(--brand-blue); color: var(--paper); }
  .card-front .wordmark {
    position: absolute; left: 0; right: 0; top: 150px;
    text-align: center; font-weight: 700; font-size: 46px; line-height: 1;
    letter-spacing: -0.5px;
  }
  .card-front .tagline {
    position: absolute; left: 0; right: 0; top: 278px;
    text-align: center; font-size: 14px; font-weight: 400;
  }

  /* Back */
  .card-back { left: 463px; top: 445px; background: var(--paper); }
  .band { position: absolute; left: 0; width: 100%; height: 25px; background: var(--brand-blue); }
  .band-top { top: 0; }
  .band-bottom { bottom: 0; }
  .band .block { position: absolute; top: 0; height: 100%; width: 134px; background: var(--accent-black); }
  .band-top .block { left: 91px; }
  .band-bottom .block { left: 424px; }

  .card-back .wordmark {
    position: absolute; left: 36px; top: 120px; width: 260px;
    font-weight: 700; font-size: 40px; line-height: 1.05; color: var(--ink);
  }
  .card-back .tagline {
    position: absolute; left: 36px; top: 265px;
    font-size: 11px; color: var(--muted);
  }

  .contact { position: absolute; left: 317px; top: 98px; width: 320px; }
  .contact .name { color: var(--brand-blue); font-weight: 700; font-size: 22px; line-height: 1; }
  .contact .role { color: var(--muted); font-size: 21px; margin-top: 8px; line-height: 1; }
  .contact .address { color: var(--ink); font-size: 18px; line-height: 23px; margin-top: 50px; }
  .contact .lines { list-style: none; margin-top: 14px; }
  .contact .lines li {
    display: flex; align-items: center; gap: 8px;
    color: var(--ink); font-size: 16px; height: 26px; white-space: nowrap;
  }
  .contact .icon { width: 16px; height: 16px; flex: none; }
</style>
</head>
<body>

<section class="card card-front" aria-label="Card front">
  <div class="wordmark">TechHollow<br>Solutions</div>
  <p class="tagline">Business Technology Services and Consulting</p>
</section>

<section class="card card-back" aria-label="Card back">
  <div class="band band-top"><span class="block"></span></div>

  <div class="wordmark">TechHollow<br>Solutions</div>
  <p class="tagline">Business Technology Services and Consulting</p>

  <div class="contact">
    <p class="name">Garrett L. Ostrander</p>
    <p class="role">Owner</p>
    <p class="address">TechHollow Solutions 2817<br>Marwood Lane Brevard, NY 13592</p>
    <ul class="lines">
      <li>
        <svg class="icon" viewBox="0 0 16 16" aria-hidden="true">
          <rect width="16" height="16" fill="#2262ab"/>
          <path d="M5 4h2l1 2-1.2 1a5 5 0 0 0 2.2 2.2L10 8l2 1v2c0 .6-.5 1-1 1A7 7 0 0 1 4 5c0-.5.4-1 1-1z" fill="#fff"/>
        </svg>
        (917) 555-0147
      </li>
      <li>
        <svg class="icon" viewBox="0 0 16 16" aria-hidden="true">
          <rect width="16" height="16" fill="#2262ab"/>
          <rect x="3" y="4.5" width="10" height="7" fill="none" stroke="#fff" stroke-width="1.2"/>
          <path d="M3 4.5l5 4 5-4" fill="none" stroke="#fff" stroke-width="1.2"/>
        </svg>
        gostrander@techhollowsolutions.example
      </li>
      <li>
        <svg class="icon" viewBox="0 0 16 16" aria-hidden="true">
          <rect width="16" height="16" fill="#2262ab"/>
          <circle cx="8" cy="8" r="4.5" fill="none" stroke="#fff" stroke-width="1.2"/>
          <ellipse cx="8" cy="8" rx="2" ry="4.5" fill="none" stroke="#fff" stroke-width="1"/>
          <path d="M3.5 8h9" stroke="#fff" stroke-width="1"/>
        </svg>
        www.techhollowsolutions.example
      </li>
    </ul>
  </div>

  <div class="band band-bottom"><span class="block"></span></div>
</section>

</body>
</html>
```